Upsell Vertical Banner Ad Design For B2B Marketing Agency Vertical 768px × 1180px IS THE SIZE

I need a banner made for my website www.brightlanepromotionhub.biz This banner will be an upsell advertisement for after someone signs up for my monthly program. When they login to their account for the 1st time I will give them the chance to upgrade their account to our annual program with just one click.

this is a page that upsells it currently to give you an idea how we market ourselves:
https://tlpx.pagevault-example.com/page/tlp-annual-upsell

Use this content:

Are You Ready To Commit To Taking Your Business To The Next Level?

Because We're In This For The Long-Haul and Dedicated To Your Success...

Save $300 By Upgrading To An Annual Membership And Pay Only $74/mth

((BUTTON))Yes, Upgrade My Plan Right Now!

*Must prepay the full year at only $898/yr!

Target Market(s)

business owners

Industry/Entity Type

Marketing

Requirements
Must have
• 768px × 1180px IS THE SIZE vertical

Use this content:

Nice to have
• Use this content:

Should not have
• Use this content:

```html
<!DOCTYPE html>
<html lang="en">
<head>
<meta charset="utf-8">
<title>Bright Lane Promotion Hub – Annual Membership Upgrade</title>
<link rel="stylesheet" href="https://fonts.googleapis.com/css2?family=Open+Sans:wght@400;600&family=Roboto:wght@500;700;900&display=swap">
<style>
  :root {
    --paint-red: #f0364f;
    --paint-pink: #ee3f6c;
    --paint-magenta: #c93873;
    --paint-plum: #5a2f6a;
    --paint-navy: #3a2a5c;
    --ink-blush: #f4c9c2;
    --brand-blue: #1c74c2;
    --button-blue: #1a72c0;
    --white: #ffffff;
    --patch: rgba(235, 220, 235, 0.55);
  }
  * { margin: 0; padding: 0; box-sizing: border-box; }
  html, body { width: 781px; height: 1200px; overflow: hidden; }
  body { background: var(--paint-navy); }

  .banner {
    position: relative;
    width: 781px;
    height: 1200px;
    overflow: hidden;
    font-family: "Open Sans", Arial, sans-serif;
  }

  .banner__artwork {
    position: absolute;
    inset: 0;
    background:
      radial-gradient(ellipse 420px 300px at 200px 260px, rgba(238, 63, 108, 0.9), transparent 70%),
      radial-gradient(ellipse 500px 420px at 560px 180px, rgba(240, 54, 79, 0.85), transparent 70%),
      radial-gradient(ellipse 360px 500px at 560px 720px, rgba(201, 56, 115, 0.7), transparent 70%),
      radial-gradient(ellipse 380px 340px at 110px 620px, rgba(240, 54, 79, 0.75), transparent 70%),
      linear-gradient(180deg, var(--paint-pink) 0%, var(--paint-red) 35%, var(--paint-magenta) 58%, var(--paint-plum) 82%, var(--paint-navy) 100%);
  }

  .brand {
    position: absolute;
    left: 108px;
    top: 70px;
    padding: 14px 22px 14px 16px;
    background: var(--patch);
    display: flex;
    align-items: center;
    gap: 10px;
  }
  .brand__mark {
    width: 18px;
    height: 18px;
    border-radius: 50%;
    background: var(--brand-blue);
  }
  .brand__name {
    font-family: "Roboto", Arial, sans-serif;
    font-weight: 700;
    font-size: 22px;
    letter-spacing: 1.5px;
    text-transform: uppercase;
    color: var(--brand-blue);
  }

  .intro {
    position: absolute;
    left: 99px;
    top: 228px;
    width: 640px;
    color: var(--ink-blush);
    font-size: 22px;
    line-height: 31px;
    letter-spacing: 1px;
    text-transform: uppercase;
  }
  .intro__line + .intro__line { margin-top: 27px; }

  .offer {
    position: absolute;
    left: 0;
    top: 0;
    font-family: "Roboto", Arial, sans-serif;
    font-weight: 900;
    color: var(--white);
    text-transform: uppercase;
  }
  .offer__row { position: absolute; white-space: nowrap; }
  .offer__small { font-size: 19px; font-weight: 700; margin-right: 6px; }
  .offer__big { font-size: 31px; letter-spacing: 0.5px; }
  .offer__tag {
    display: inline-block;
    background: var(--brand-blue);
    color: var(--white);
  }
  .offer__row--save { left: 117px; top: 484px; }
  .offer__row--save .offer__tag { font-size: 28px; font-weight: 700; width: 229px; height: 40px; line-height: 40px; padding-left: 12px; }
  .offer__row--upgrade { left: 121px; top: 528px; }
  .offer__row--annual { left: 121px; top: 570px; }
  .offer__row--price { left: 121px; top: 617px; display: flex; align-items: center; }
  .offer__row--price .offer__tag { font-size: 36px; font-weight: 700; height: 50px; line-height: 50px; padding: 0 12px 0 12px; width: 424px; letter-spacing: 0.5px; }

  .cta {
    position: absolute;
    left: 100px;
    top: 776px;
    width: 347px;
    height: 70px;
    border-radius: 6px;
    background: var(--button-blue);
    color: var(--white);
    font-family: "Roboto", Arial, sans-serif;
    font-size: 21px;
    line-height: 26px;
    font-weight: 500;
    text-transform: uppercase;
    text-align: center;
    text-decoration: none;
    display: flex;
    flex-direction: column;
    justify-content: center;
  }
  .cta strong { font-weight: 700; }

  .terms {
    position: absolute;
    left: 99px;
    top: 1133px;
    color: var(--ink-blush);
    font-size: 20px;
    letter-spacing: 1px;
    text-transform: uppercase;
  }
</style>
</head>
<body>
  <main class="banner">
    <div class="banner__artwork" role="img" aria-label="Abstract acrylic painting in bold red, pink and deep purple brush strokes"></div>

    <div class="brand">
      <span class="brand__mark"></span>
      <span class="brand__name">Bright Lane Promotion Hub</span>
    </div>

    <div class="intro">
      <p class="intro__line">Are you ready to commit to taking your<br>business to the next level?</p>
      <p class="intro__line">Because we’re in this for the long-haul<br>and dedicated to your success…</p>
    </div>

    <div class="offer">
      <div class="offer__row offer__row--save"><span class="offer__tag">Save $300</span></div>
      <div class="offer__row offer__row--upgrade"><span class="offer__small">By</span><span class="offer__big">Upgrading</span></div>
      <div class="offer__row offer__row--annual"><span class="offer__small">To</span><span class="offer__big">An Annual Membership</span></div>
      <div class="offer__row offer__row--price"><span class="offer__small">And</span><span class="offer__tag">Pay Only $74/mth</span></div>
    </div>

    <a class="cta" href="https://tlpx.pagevault-example.com/page/tlp-annual-upsell">
      <span><strong>Yes,</strong> Upgrade My Plan</span>
      <strong>Right Now!</strong>
    </a>

    <p class="terms">*Must prepay the full year at only $898/yr!</p>
  </main>
</body>
</html>
```